Business Card - Cooperate

Business Card for Larkfield Management Consulting

Target Market(s)

Corparte - b2B

Industry/Entity Type

Management Consulting - Professional Services

Contact Information for Business Card

Company Name , Slogan , Dummy Address,

Requirements
Must have
• Reach your Full Potential

```html
<!DOCTYPE html>
<html lang="en">
<head>
<meta charset="utf-8">
<title>Larkfield Management Consulting – Business Card</title>
<link href="https://fonts.googleapis.com/css2?family=Montserrat:wght@400;500;700;800&display=swap" rel="stylesheet">
<style>
  :root {
    --bg: #9b9b9b;
    --white: #ffffff;
    --navy: #17237d;
    --brand-blue: #1450c8;
    --teal: #1a9a82;
    --blue-dark: #1b2488;
    --blue-light: #0388f5;
    --green-light: #72d610;
    --green-dark: #22b52b;
  }
  * { box-sizing: border-box; margin: 0; padding: 0; }
  html, body {
    width: 1133px; height: 1200px; overflow: hidden;
    background: var(--bg);
    font-family: "Montserrat", sans-serif;
  }
  .card {
    position: absolute; left: 200px; width: 734px; height: 418px;
  }
  .card--front { top: 120px; background: var(--white); }
  .card--back { top: 620px; background: var(--navy); }

  .brand {
    position: absolute; left: 0; right: 0; top: 88px;
    display: flex; flex-direction: column; align-items: center;
  }
  .brand__row { display: flex; align-items: center; gap: 16px; }
  .brand__dot {
    width: 40px; height: 40px; border-radius: 50%; background: var(--brand-blue);
  }
  .brand__name {
    font-size: 56px; font-weight: 700; color: var(--brand-blue); line-height: 1;
    letter-spacing: 0.5px;
  }
  .brand__tagline {
    margin-top: 12px; font-size: 12.5px; font-weight: 700; color: var(--teal);
    letter-spacing: 2.4px;
  }

  .band {
    position: absolute; top: 259px; bottom: 0; color: var(--white);
  }
  .band--person {
    left: 0; width: 382px;
    background: linear-gradient(90deg, var(--blue-dark) 15%, var(--blue-light) 95%);
    padding: 26px 0 0 50px;
  }
  .band--contact {
    left: 385px; right: 0;
    background: linear-gradient(90deg, var(--green-light) 35%, var(--green-dark) 100%);
    padding: 34px 54px 0 0;
  }
  .person__name { font-size: 22px; font-weight: 700; line-height: 1.2; }
  .person__role { font-size: 15px; margin-top: 2px; }
  .person__address { font-size: 15px; margin-top: 10px; line-height: 1.4; font-style: normal; }

  .contact { list-style: none; text-align: right; }
  .contact__item {
    display: flex; justify-content: flex-end; align-items: center; gap: 8px;
    font-size: 15px; line-height: 21px;
  }
  .contact__icon { width: 14px; height: 14px; fill: var(--white); flex: none; }

  .back__mark {
    position: absolute; left: 0; right: 0; top: 150px;
    display: flex; justify-content: center; align-items: center; gap: 16px;
  }
  .back__dot { width: 44px; height: 44px; border-radius: 50%; background: #3d5cff; }
  .back__name { font-size: 60px; font-weight: 700; color: var(--white); line-height: 1; }
  .back__tagline {
    position: absolute; left: 0; right: 0; top: 363px; text-align: center;
    color: var(--white); font-size: 15.5px; font-weight: 500;
  }
</style>
</head>
<body>
  <section class="card card--front">
    <div class="brand">
      <div class="brand__row">
        <span class="brand__dot"></span>
        <span class="brand__name">Larkfield</span>
      </div>
      <p class="brand__tagline">REACH YOUR FULL POTENTIAL</p>
    </div>

    <div class="band band--person">
      <p class="person__name">Daniel Harper</p>
      <p class="person__role">President</p>
      <address class="person__address">4210 Willowbend Road<br>Fairview, Oregon 97024</address>
    </div>

    <div class="band band--contact">
      <ul class="contact">
        <li class="contact__item">555-214-7730
          <svg class="contact__icon" viewBox="0 0 16 16"><path d="M3.5 1l2.5 0 1 3.5-1.6 1.2c.8 1.8 2.1 3.1 3.9 3.9l1.2-1.6 3.5 1v2.5c0 1-1 1.5-2 1.5C6.5 13 3 9.5 2 4.5 2 2 2.5 1 3.5 1z"/></svg>
        </li>
        <li class="contact__item">555-318-4092
          <svg class="contact__icon" viewBox="0 0 16 16"><path d="M4 0h8a1 1 0 0 1 1 1v14a1 1 0 0 1-1 1H4a1 1 0 0 1-1-1V1a1 1 0 0 1 1-1zm.8 1.6v11.4h6.4V1.6z"/></svg>
        </li>
        <li class="contact__item">info@larkfield.com
          <svg class="contact__icon" viewBox="0 0 16 16"><path d="M1 3h14v10H1zm1.5 1.2L8 8.5l5.5-4.3z"/></svg>
        </li>
        <li class="contact__item">www.larkfield.com
          <svg class="contact__icon" viewBox="0 0 16 16"><path d="M8 0a8 8 0 1 0 0 16A8 8 0 0 0 8 0zm-4.5 4h3l1 2-2 2 1 3-2 2C2.5 11.5 2 9 3.5 4zm6 1l3-1.5c1.5 1.5 2 4 1 6.5l-2-1-1-2z"/></svg>
        </li>
      </ul>
    </div>
  </section>

  <section class="card card--back">
    <div class="back__mark">
      <span class="back__dot"></span>
      <span class="back__name">Larkfield</span>
    </div>
    <p class="back__tagline">Reach your Full Potential</p>
  </section>
</body>
</html>
```